Golden Years Wellness Roadmap: This is my second book. The first was Eldercare Compass

I need a book cover design for: GOLDEN YEARS WELLNESS ROADMAP: A NO-EXPENSE METHOD FOR FINISHING YOUR LATER-LIFE MOSAIC WITH POOLED KVB CARE SCHEMES by Derek Holloway Neil Osgrove & Martin Quarles. This book is designed for business owners, CEO's, CFO's and Human Resources. The cover needs to be professional and focused on business. The purpose of this book is to educate business owners and their management about a zero cost retiree health plan. This is a first of it's kind solution that every business needs to learn about.

Target Market(s)

Business owners, CEO's, CFO's and Human Resources

Requirements
Nice to have
• I want the design to be clean and professional since it is focused on business executives

```html
<!DOCTYPE html>
<html lang="en">
<head>
<meta charset="utf-8">
<title>Golden Years Wellness Roadmap — Book Cover</title>
<link rel="stylesheet" href="https://fonts.googleapis.com/css2?family=Jost:ital,wght@0,300;1,400&family=Open+Sans:wght@600&display=swap">
<style>
  :root {
    --page-bg: #e9e6e1;
    --cover-black: #050608;
    --band-navy: #0d1a2e;
    --art-deep: #0a1a33;
    --art-mid: #1c4a8a;
    --art-glow: #7fb2ee;
    --text-white: #f4f6f8;
    --text-soft: #d9dee6;
  }
  * { margin: 0; padding: 0; box-sizing: border-box; }
  html, body {
    width: 1200px;
    height: 1200px;
    overflow: hidden;
    background: var(--page-bg);
  }
  .stage {
    width: 1200px;
    height: 1200px;
    display: flex;
    align-items: center;
    justify-content: center;
  }
  .book-cover {
    position: relative;
    width: 625px;
    height: 1120px;
    background: var(--cover-black);
    overflow: hidden;
  }
  .cover-art {
    position: absolute;
    left: 0;
    top: 0;
    width: 100%;
    height: 540px;
    background:
      radial-gradient(ellipse 55% 30% at 70% 72%, rgba(127,178,238,0.55), transparent 70%),
      radial-gradient(ellipse 50% 40% at 25% 30%, rgba(28,74,138,0.7), transparent 75%),
      linear-gradient(180deg, var(--art-deep) 0%, var(--art-mid) 55%, var(--art-deep) 80%, var(--cover-black) 100%);
  }
  .title {
    position: absolute;
    left: 77px;
    top: 560px;
    font-family: "Jost", sans-serif;
    font-weight: 300;
    font-size: 64px;
    line-height: 88px;
    letter-spacing: 0.04em;
    color: var(--text-white);
    text-transform: uppercase;
  }
  .title span { display: block; }
  .subtitle {
    position: absolute;
    left: 0;
    right: 0;
    top: 908px;
    text-align: center;
    font-family: "Jost", sans-serif;
    font-style: italic;
    font-weight: 400;
    font-size: 18px;
    line-height: 27px;
    color: var(--text-soft);
  }
  .author-band {
    position: absolute;
    left: 0;
    bottom: 0;
    width: 100%;
    height: 135px;
    background: var(--band-navy);
    display: flex;
    align-items: center;
    justify-content: center;
  }
  .authors {
    font-family: "Open Sans", sans-serif;
    font-weight: 600;
    font-size: 17px;
    color: var(--text-white);
    letter-spacing: 0.01em;
  }
  .authors .sep { margin: 0 9px; }
</style>
</head>
<body>
  <main class="stage">
    <section class="book-cover">
      <div class="cover-art" role="img" aria-label="Abstract blue digital network of glowing connected lines, data charts and plexus shapes on a dark background"></div>

      <h1 class="title">
        <span>Golden Years</span>
        <span>Wellness</span>
        <span>Roadmap</span>
      </h1>

      <p class="subtitle">A No-Expense Method for Finishing Your<br>Later-Life Mosaic with Pooled KVB Care Schemes</p>

      <footer class="author-band">
        <p class="authors">Derek Holloway<span class="sep">•</span>Neil Osgrove<span class="sep">•</span>Martin Quarles</p>
      </footer>
    </section>
  </main>
</body>
</html>
```